InnRiderz Web Temp | ||
Web Temp | ||
Transportation | ||
www.innriderz.example | ||
Inn Riderz provides transportation from the top hotels around the world to the airports and vice versa. | ||
I would like to see a clean website, which looks very professional and inspires confidence in the user that the service is outstanding. It needs to look good with our logo, which has been uploaded for your reference. I would like the designer to include the text at the bottom of the pdf file that was uploaded. Additionally, there should be an area on the site that states, "Book Hotels, Flights...." followed by a buttom and "powered by trovask" |
Professional Sophisticated Corporate Modern Elegant |
below header | ||
trovask.example | ||
global-gate-shuttle.example | ||
pelunta.example | ||
Similar to trovask and pelunta, the site needs to be engaging. Most importantly it needs to show the following drop down input fields. (1) Select a country (2) Select a city (3) Rountrip (followed by circle that users can select) (4) One Way (followed by circle that users can select) (5) Select Hotel (drop down menu) (6) Select airport (drop down menu) (7) Arriving/Departing (pop up calendar). I have uploaded another file with a very crude mock up. But the text at the bottom of that sample should be included. I would like the designer to include the text at the bottom of the pdf file that was uploaded. Additionally, there should be an area on the site that states, "Book Hotels, Flights...." followed by a buttom and "powered by trovask" |

```html
<!DOCTYPE html>
<html lang="en">
<head>
<meta charset="utf-8">
<title>Inn Riderz — Worldwide Hotel Transportation</title>
<link href="https://fonts.googleapis.com/css2?family=Open+Sans:wght@400;600;700&display=swap" rel="stylesheet">
<style>
  :root{
    --night-deep:#07090f;
    --night-mid:#1b2230;
    --night-glow:#5a4a38;
    --topbar:#111318;
    --header-white:#f4f5f7;
    --brand-navy:#1f3a6b;
    --nav-top:#5a5c60;
    --nav-bottom:#2f3033;
    --panel:rgba(40,42,46,.88);
    --panel-head:#8c8f94;
    --package:#4a4c50;
    --package-active:#5f6166;
    --text-light:#e8e9eb;
    --text-dim:#b9bcc1;
    --field:#f2f2f2;
    --field-text:#333;
    --sky:#2f6fc4;
    --sea:#123e78;
    --footer:#202226;
  }
  *{box-sizing:border-box;margin:0;padding:0}
  html,body{width:1200px;height:804px;overflow:hidden}
  body{font-family:"Open Sans",Arial,sans-serif;color:var(--text-light);position:relative;background:var(--night-deep)}
  .backdrop{position:absolute;inset:0;
    background:radial-gradient(ellipse at 50% 88%,var(--night-glow) 0%,rgba(90,74,56,0) 45%),
               linear-gradient(180deg,#0c0f16 0%,var(--night-mid) 55%,#2b2218 82%,#0b0b0d 100%)}
  .topbar{position:absolute;left:0;top:0;width:1200px;height:29px;background:var(--topbar);font-size:12px;color:var(--text-light)}
  .topbar .locale{position:absolute;left:163px;top:6px}
  .topbar .account{position:absolute;left:888px;top:6px}
  .topbar .sep{color:#777;margin:0 6px}
  .site-header{position:absolute;left:134px;top:29px;width:922px;height:110px;background:var(--header-white)}
  .brand{position:absolute;left:30px;top:26px;display:flex;align-items:center;gap:12px}
  .brand-dot{width:48px;height:48px;border-radius:50%;background:var(--brand-navy)}
  .brand-name{font-size:32px;font-weight:700;color:var(--brand-navy);line-height:1}
  .brand-tagline{position:absolute;left:90px;top:78px;font-size:9px;letter-spacing:1px;color:#555;font-weight:600}
  .social{position:absolute;right:24px;top:14px;display:flex;gap:6px}
  .social span{width:24px;height:24px;border-radius:4px;background:#3b5c98}
  .social span:first-child{background:#3aa6d8}
  .social span:last-child{background:#c22a22}
  .main-nav{position:absolute;left:134px;top:139px;width:922px;height:36px;background:linear-gradient(var(--nav-top),var(--nav-bottom));font-size:15px}
  .main-nav a{position:absolute;top:8px;color:#fff;text-decoration:none}
  .search{position:absolute;left:747px;top:6px;width:151px;height:24px;border-radius:12px;background:#fff;color:#888;font-size:11px;padding:4px 12px}
  .search svg{position:absolute;right:9px;top:6px}
  .trip-panel{position:absolute;left:134px;top:192px;width:389px;height:355px;background:var(--panel)}
  .trip-panel h2{height:29px;background:var(--panel-head);font-size:12px;font-weight:400;letter-spacing:.5px;padding:6px 24px;color:#fff}
  .opt{position:absolute;font-size:12px;display:flex;align-items:center;gap:8px}
  .box{width:11px;height:11px;background:#fff}
  .dot{width:11px;height:11px;border-radius:50%;background:#fff}
  .label{position:absolute;font-size:12px}
  .field{position:absolute;height:22px;background:var(--field);color:var(--field-text);font-size:10px;padding:4px 6px;border-radius:2px}
  .field::after{content:"";position:absolute;right:6px;top:9px;border:4px solid transparent;border-top-color:#444}
  .more{position:absolute;left:29px;top:300px;font-size:12px}
  .plan-btn{position:absolute;left:226px;top:288px;width:132px;height:26px;border-radius:13px;background:#f4f4f4;color:#222;font-size:12px;text-align:center;line-height:26px}
  .powered{position:absolute;left:250px;top:331px;font-size:9px;color:#ddd}
  .powered b{font-size:12px;color:#fff;margin-left:4px}
  .feature-photo{position:absolute;left:547px;top:197px;width:298px;height:350px;background:linear-gradient(180deg,var(--sky) 0%,#7fb0e6 55%,var(--sea) 70%,#0c2b57 100%)}
  .packages{position:absolute;left:859px;top:197px;width:187px;list-style:none}
  .packages li{height:44px;margin-bottom:7px;background:var(--package);color:#fff;font-size:12px;text-align:center;line-height:44px}
  .packages li.active{background:var(--package-active)}
  .deals-head{position:absolute;left:134px;top:562px;width:922px;height:28px;background:var(--panel-head);font-size:12px;padding:5px 24px;color:#fff}
  .deals{position:absolute;left:154px;top:600px;display:flex;gap:19px}
  .deal{width:130px;height:125px;position:relative;background:#333}
  .deal .img{height:125px}
  .deal span{position:absolute;left:0;bottom:0;width:100%;height:28px;background:rgba(0,0,0,.55);font-size:12px;padding:6px 8px;color:#fff}
  .site-footer{position:absolute;left:134px;top:758px;width:922px;height:46px;background:var(--footer);font-size:12px}
  .site-footer .to-top{position:absolute;left:24px;top:14px}
  .site-footer .rights{position:absolute;right:24px;top:14px}
</style>
</head>
<body>
<div class="backdrop" role="img" aria-label="Night city skyline with glowing lights"></div>

<div class="topbar">
  <div class="locale">USD ($) ▾<span class="sep">|</span>English (US) ▾</div>
  <div class="account">Sign in<span class="sep">|</span>Sign up<span class="sep">|</span>Help</div>
</div>

<header class="site-header">
  <div class="brand"><span class="brand-dot"></span><span class="brand-name">Inn Riderz</span></div>
  <div class="brand-tagline">WORLDWIDE HOTEL TRANSPORTATION</div>
  <div class="social" aria-label="Social links"><span></span><span></span><span></span></div>
</header>

<nav class="main-nav">
  <a style="left:27px">HOME</a>
  <a style="left:106px">ABOUT</a>
  <a style="left:190px">SERVICES</a>
  <a style="left:298px">LOCATIONS</a>
  <a style="left:418px">AFFILIATES</a>
  <a style="left:536px">CONTACT</a>
  <div class="search">Search
    <svg width="12" height="12" viewBox="0 0 12 12"><circle cx="5" cy="5" r="3.6" fill="none" stroke="#666" stroke-width="1.5"/><line x1="7.6" y1="7.6" x2="11" y2="11" stroke="#666" stroke-width="1.6"/></svg>
  </div>
</nav>

<section class="trip-panel">
  <h2>PLAN YOUR TRIP</h2>
  <div class="opt" style="left:29px;top:45px"><span class="box"></span>Book a car</div>
  <div class="opt" style="left:29px;top:67px"><span class="box"></span>Book a flight</div>
  <div class="opt" style="left:29px;top:89px"><span class="box"></span>Book a hotel</div>
  <div class="opt" style="left:209px;top:45px"><span class="dot"></span>One way</div>
  <div class="opt" style="left:209px;top:67px"><span class="dot"></span>Round trip</div>
  <div class="opt" style="left:209px;top:89px"><span class="dot"></span>Multiple Destinations</div>

  <div class="label" style="left:29px;top:121px">Leaving from</div>
  <div class="label" style="left:164px;top:121px">Departing</div>
  <div class="label" style="left:298px;top:121px">Time</div>
  <div class="field" style="left:29px;top:142px;width:120px">Drop-Down List</div>
  <div class="field" style="left:164px;top:142px;width:122px">mm/dd/yy</div>
  <div class="field" style="left:298px;top:142px;width:67px">hh:mm</div>

  <div class="label" style="left:29px;top:175px">Going to</div>
  <div class="label" style="left:164px;top:175px">Returning</div>
  <div class="label" style="left:298px;top:175px">Time</div>
  <div class="field" style="left:29px;top:195px;width:120px">Drop-Down List</div>
  <div class="field" style="left:164px;top:195px;width:122px">mm/dd/yy</div>
  <div class="field" style="left:298px;top:195px;width:67px">hh:mm</div>

  <div class="label" style="left:29px;top:228px">Children (0-17)</div>
  <div class="label" style="left:164px;top:228px">Adults (18-64)</div>
  <div class="label" style="left:298px;top:228px">Seniors (65+)</div>
  <div class="field" style="left:29px;top:247px;width:62px">2</div>
  <div class="field" style="left:164px;top:247px;width:62px">2</div>
  <div class="field" style="left:298px;top:247px;width:62px">2</div>

  <div class="more">Show Additional Options ▾</div>
  <div class="plan-btn">Plan it for me</div>
  <div class="powered">Powered by<b>trovask</b></div>
</section>

<div class="feature-photo" role="img" aria-label="Sydney harbour opera house under a blue sky"></div>

<ul class="packages">
  <li>Toronto Package</li>
  <li>Colombo Package</li>
  <li class="active">Sydney Package</li>
  <li>Tokyo Package</li>
  <li>Paris Package</li>
  <li>Montreal Package</li>
  <li>Agra Package</li>
</ul>

<div class="deals-head">TOP DEALS</div>
<div class="deals">
  <div class="deal"><div class="img" role="img" aria-label="Cruise ship at sea" style="background:linear-gradient(#8cc3ec,#3a79b8)"></div><span>Cruise Trip</span></div>
  <div class="deal"><div class="img" role="img" aria-label="Palm trees on a tropical beach" style="background:linear-gradient(#4aa3dc,#2f7a4a)"></div><span>Srilankan Palms</span></div>
  <div class="deal"><div class="img" role="img" aria-label="Casino chips" style="background:linear-gradient(#2a6fb5,#d6a21c)"></div><span>Visit Vegas</span></div>
  <div class="deal"><div class="img" role="img" aria-label="City lights at night" style="background:linear-gradient(#1c2140,#b2452a)"></div><span>Happening Seoul</span></div>
  <div class="deal"><div class="img" role="img" aria-label="Sunny beach with clear water" style="background:linear-gradient(#3c9ad8,#e0b23a)"></div><span>Hawaiian Beach</span></div>
  <div class="deal"><div class="img" role="img" aria-label="Beach umbrellas by a blue lagoon" style="background:linear-gradient(#6fb9e6,#c9b58e)"></div><span>Blue Mauritius</span></div>
</div>

<footer class="site-footer">
  <div class="to-top">▲&nbsp;&nbsp;Back to top</div>
  <div class="rights">Inn Riderz | All Rights Reserved</div>
</footer>
</body>
</html>
```